Stationery design for law/Property/finance business

We need stationery design for a Law/Property/Finance business called Stonebridge. Logo is attached.
we require a letterhead and with compliments slip.
Would like to see a very simple professional design using the colours of the logo and offset against Charcoal colours. Maybe a charcoal band for header and footer with logo and details appearing in it? Former letterhead attached for examples.
we require the project to be provided in word, pdf and jpeg format.
we require the following details on the stationery:
Cairns Phone: 07 41592036
Weipa Phone: 07 41357904
Mobile: 0427 915 384
Fax: 07 41836257
email: admin@stonebridgeholdings.com.au
ABN 52 304 781 619

```html
<!DOCTYPE html>
<html lang="en">
<head>
<meta charset="utf-8">
<title>Stonebridge Stationery</title>
<link href="https://fonts.googleapis.com/css2?family=Lato:wght@400;700&family=Great+Vibes&display=swap" rel="stylesheet">
<style>
:root{
  --charcoal:#3d3d3f;
  --blue:#1a8fd3;
  --teal:#7fd0c3;
  --paper:#ffffff;
  --ink:#2b2b2d;
  --muted:#6b6b70;
  --bg:#e4e4e6;
}
*{margin:0;padding:0;box-sizing:border-box}
html,body{width:1200px;height:1200px;overflow:hidden}
body{background:var(--bg);font-family:"Lato",sans-serif;color:var(--ink);position:relative}
.sheet{position:absolute;background:var(--paper);box-shadow:0 6px 24px rgba(0,0,0,.18);overflow:hidden}
.letterhead{left:70px;top:90px;width:600px;height:848px}
.slip{left:450px;top:640px;width:680px;height:322px}
.header-band{position:absolute;left:0;top:0;width:100%;background:var(--charcoal)}
.letterhead .header-band{height:112px}
.slip .header-band{height:92px}
.brand{position:absolute;left:34px;bottom:20px;display:flex;align-items:center;gap:10px}
.brand-mark{width:20px;height:20px;border-radius:50%;background:var(--teal)}
.brand-name{font-weight:700;font-size:28px;letter-spacing:1px;color:var(--blue);text-transform:uppercase}
.abn{position:absolute;right:34px;top:24px;color:#fff;font-size:10px;letter-spacing:.3px}
.web{position:absolute;right:34px;font-size:9px;color:var(--muted);display:flex;align-items:center;gap:6px}
.letterhead .web{top:122px}
.slip .web{top:100px}
.web svg{width:8px;height:8px}
.letter-body{position:absolute;left:60px;top:178px;width:480px;font-size:9.5px;line-height:1.45;color:var(--ink)}
.letter-date{font-size:10.5px;margin-bottom:20px}
.letter-topic{font-weight:700;font-size:11px;margin-left:12px;margin-bottom:18px}
.letter-text p{margin-left:24px;margin-bottom:10px}
.sign-off{margin-left:24px;margin-top:26px}
.sign-name{font-size:13px;line-height:1.3}
.sign-role{font-size:8.5px;font-weight:700;line-height:1.3}
.signature{margin-top:12px;width:110px;height:44px;border-radius:4px;background:linear-gradient(90deg,#dfe6ef,#eef2f6)}
.footer{position:absolute;left:0;bottom:0;width:100%;background:var(--charcoal);border-bottom:6px solid var(--blue);display:flex;align-items:center;padding:0 28px;color:#fff;font-size:10px}
.letterhead .footer{height:80px}
.slip .footer{height:76px}
.footer-col{display:flex;align-items:center;gap:14px;flex:1;white-space:nowrap}
.footer-col.primary{flex:1.35;padding-right:12px}
.footer-col + .footer-col{border-left:1px solid var(--blue);padding-left:18px}
.contact-lines{line-height:1.45}
.contact-line{display:flex;align-items:center;gap:6px}
.contact-line svg{width:8px;height:8px;fill:var(--blue)}
.postal{line-height:1.45}
.town{color:var(--blue)}
.compliments{position:absolute;left:70px;top:150px;font-family:"Great Vibes",cursive;font-size:54px;color:var(--ink)}
</style>
</head>
<body>

<section class="sheet letterhead">
  <header class="header-band">
    <div class="brand"><span class="brand-mark"></span><span class="brand-name">Stonebridge</span></div>
    <div class="abn">ABN 52 304 781 619</div>
  </header>
  <div class="web"><svg viewBox="0 0 10 10"><circle cx="5" cy="5" r="5" fill="#1a8fd3"/></svg>www.stonebridgeholdings.com.au</div>

  <div class="letter-body">
    <div class="letter-date">Weipa, 01. 01. 2016.</div>
    <div class="letter-topic">Today’s topic</div>
    <div class="letter-text">
      <p>Lorem ipsum dolor sit amet, consectetur adipisicing elit, sed do eiusmod tempor incididunt ut labore et dolore magna aliqua. Ut enim ad minim veniam, quis nostrud exercitation ullamco laboris nisi ut aliquip ex ea commodo consequat.</p>
      <p>Duis aute irure dolor in reprehenderit in voluptate velit esse cillum dolore eu fugiat nulla pariatur. Excepteur sint occaecat cupidatat non proident, sunt in culpa qui officia deserunt mollit anim id est laborum.</p>
      <p>Sed ut perspiciatis unde omnis iste natus error sit voluptatem accusantium doloremque laudantium, totam rem aperiam, eaque ipsa quae ab illo inventore veritatis et quasi architecto beatae vitae dicta sunt explicabo.</p>
      <p>Nemo enim ipsam voluptatem quia voluptas sit aspernatur aut odit aut fugit, sed quia consequuntur magni dolores eos qui ratione voluptatem sequi nesciunt. Neque porro quisquam est, qui dolorem ipsum quia dolor sit amet, consectetur, adipisci velit.</p>
      <p>Ut enim ad minima veniam, quis nostrum exercitationem ullam corporis suscipit laboriosam, nisi ut aliquid ex ea commodi consequatur.</p>
      <p>Quis autem vel eum iure reprehenderit qui in ea voluptate velit esse quam nihil molestiae consequatur, vel illum qui dolorem eum fugiat.</p>
      <p>Duis aute irure dolor in reprehenderit in voluptate velit esse cillum dolore eu fugiat nulla pariatur. Excepteur sint occaecat cupidatat non proident.</p>
      <p>Lorem ipsum dolor sit amet, consectetur adipisicing elit, sed do eiusmod tempor incididunt ut labore et dolore magna aliqua. Ut enim ad minim veniam, quis nostrud exercitation.</p>
    </div>
    <div class="sign-off">
      <div class="sign-name">Daniel Hale</div>
      <div class="sign-role">Business Manager</div>
      <div class="signature" role="img" aria-label="Handwritten signature"></div>
    </div>
  </div>

  <footer class="footer">
    <div class="footer-col primary">
      <div class="contact-lines">
        <div class="contact-line"><svg viewBox="0 0 10 10"><rect x="2" y="0" width="6" height="10" rx="1"/></svg>0427 915 384</div>
        <div class="contact-line"><svg viewBox="0 0 10 10"><rect x="0" y="2" width="10" height="6"/></svg>admin@stonebridgeholdings.com.au</div>
      </div>
    </div>
    <div class="footer-col">
      <div class="contact-lines">
        <div class="contact-line"><svg viewBox="0 0 10 10"><path d="M2 0l2 2-1 2 3 3 2-1 2 2-2 2C4 10 0 6 0 2z"/></svg>41592036</div>
        <div class="contact-line"><svg viewBox="0 0 10 10"><rect x="0" y="3" width="10" height="7"/><rect x="2" y="0" width="6" height="3"/></svg>41836257</div>
      </div>
      <div class="postal">PO Box 2736<br><span class="town">Cairns</span> Qld 4870</div>
    </div>
    <div class="footer-col">
      <div class="contact-lines">
        <div class="contact-line"><svg viewBox="0 0 10 10"><path d="M2 0l2 2-1 2 3 3 2-1 2 2-2 2C4 10 0 6 0 2z"/></svg>41357904</div>
        <div class="contact-line"><svg viewBox="0 0 10 10"><rect x="0" y="3" width="10" height="7"/><rect x="2" y="0" width="6" height="3"/></svg>41836257</div>
      </div>
      <div class="postal">PO Box 618<br><span class="town">Weipa</span> Qld 4874</div>
    </div>
  </footer>
</section>

<section class="sheet slip">
  <header class="header-band">
    <div class="brand"><span class="brand-mark"></span><span class="brand-name">Stonebridge</span></div>
    <div class="abn">ABN 52 304 781 619</div>
  </header>
  <div class="web"><svg viewBox="0 0 10 10"><circle cx="5" cy="5" r="5" fill="#1a8fd3"/></svg>www.stonebridgeholdings.com.au</div>

  <div class="compliments">With compliments</div>

  <footer class="footer">
    <div class="footer-col primary">
      <div class="contact-lines">
        <div class="contact-line"><svg viewBox="0 0 10 10"><rect x="2" y="0" width="6" height="10" rx="1"/></svg>0427 915 384</div>
        <div class="contact-line"><svg viewBox="0 0 10 10"><rect x="0" y="2" width="10" height="6"/></svg>admin@stonebridgeholdings.com.au</div>
      </div>
    </div>
    <div class="footer-col">
      <div class="contact-lines">
        <div class="contact-line"><svg viewBox="0 0 10 10"><path d="M2 0l2 2-1 2 3 3 2-1 2 2-2 2C4 10 0 6 0 2z"/></svg>41592036</div>
        <div class="contact-line"><svg viewBox="0 0 10 10"><rect x="0" y="3" width="10" height="7"/><rect x="2" y="0" width="6" height="3"/></svg>41836257</div>
      </div>
      <div class="postal">PO Box 2736<br><span class="town">Cairns</span> Qld 4870</div>
    </div>
    <div class="footer-col">
      <div class="contact-lines">
        <div class="contact-line"><svg viewBox="0 0 10 10"><path d="M2 0l2 2-1 2 3 3 2-1 2 2-2 2C4 10 0 6 0 2z"/></svg>41357904</div>
        <div class="contact-line"><svg viewBox="0 0 10 10"><rect x="0" y="3" width="10" height="7"/><rect x="2" y="0" width="6" height="3"/></svg>41836257</div>
      </div>
      <div class="postal">PO Box 618<br><span class="town">Weipa</span> Qld 4874</div>
    </div>
  </footer>
</section>

</body>
</html>
```